Multi Page Booklet/Brochure- Cataloogue requested for Tervik

We have an industrial packaging company that has a product listing that needs to have a product feature catalog. It could also be a multiple page brochure with features and benefits of the product. Our main core products are:
Gaylord Boxes
FIBC Bulk Bags
Stretch Film
Packaging Tape
Liners

We would like to have a 2-3 page layout of each section that shows the features and benefits.

We are in the middle of a web site redesign, but you can look at our current web site that will show our products and business.

We will want photos, but don't have a lot and may need to have that done to add to the brochure.
Updates

                                        To get more information on the company, please look at tervikinc.example

This site is our old site but will give you a good reference of our products.  The new site in still on a test site and under construction.

Target Market(s)

Manufactures of any product, recycling companies (Plastic, metal, textile etc..), food processors, mining companies, oil companies

Industry/Entity Type

Industrial

Requirements
Must have
• Must be able to be bound like a book or magazine.
• Must have Feature pages of each product with Features and Benefits, then the line of product with images.

```html
<!DOCTYPE html>
<html lang="en">
<head>
<meta charset="utf-8">
<title>Tervik Enterprises – Product Catalogue Cover</title>
<link rel="stylesheet" href="https://fonts.googleapis.com/css2?family=Nunito:wght@300;800;900&family=Fira+Sans+Extra+Condensed:wght@300;700&display=swap">
<style>
  :root {
    --navy: #0d3f86;
    --blue-deep: #0b4694;
    --blue-mid: #1f62ae;
    --blue-light: #4b8fd0;
    --sky: #dcebf7;
    --yellow: #ffe400;
    --white: #ffffff;
    --logo-ink: #1d2f78;
  }
  html, body { margin: 0; padding: 0; overflow: hidden; background: #e9edf2; }
  .cover {
    position: relative;
    width: 848px; height: 1200px;
    overflow: hidden;
    font-family: "Nunito", "Arial Rounded MT Bold", sans-serif;
    color: var(--white);
  }
  .cover__art { position: absolute; inset: 0; }

  .brand { position: absolute; left: 136px; top: 78px; width: 400px; height: 100px; }
  .brand__mark { position: absolute; left: 0; top: 6px; width: 62px; height: 62px; background: var(--logo-ink); }
  .brand__name {
    position: absolute; left: 80px; top: 0;
    font-weight: 800; font-size: 54px; line-height: 1; letter-spacing: 3px;
    color: var(--logo-ink);
  }
  .brand__sub {
    position: absolute; left: 92px; top: 60px;
    font-weight: 800; font-size: 15px; line-height: 1; letter-spacing: 7.5px;
    color: var(--logo-ink);
  }
  .brand__tagline {
    position: absolute; left: 124px; top: 84px; margin: 0;
    font-size: 7.5px; font-weight: 800; white-space: nowrap; color: var(--logo-ink);
  }

  .headline { position: absolute; left: 44px; top: 298px; margin: 0; line-height: 1; }
  .headline span { position: absolute; white-space: nowrap; }
  .h-quality { left: 0; top: 0; font-size: 62px; font-weight: 900; }
  .h-of { left: 152px; top: 68px; font-size: 30px; font-weight: 300; }
  .h-products { left: 114px; top: 82px; font-size: 42px; font-weight: 900; }
  .h-and1 { left: 34px; top: 118px; font-size: 30px; font-weight: 300; }
  .h-services { left: 115px; top: 113px; font-size: 42px; font-weight: 900; }
  .h-and2 { left: 250px; top: 152px; font-size: 30px; font-weight: 300; }
  .h-quantity { left: 2px; top: 202px; font-size: 31px; font-weight: 900; }

  .source { position: absolute; left: 0; top: 0; font-family: "Fira Sans Extra Condensed", sans-serif; }
  .source span { position: absolute; white-space: nowrap; line-height: 1; }
  .s-your { left: 64px; top: 808px; font-size: 28px; font-weight: 300; }
  .s-source { left: 64px; top: 830px; font-size: 30px; font-weight: 300; letter-spacing: 1px; }
  .s-one { left: 165px; top: 762px; font-size: 122px; font-weight: 700; color: var(--yellow); }
  .s-for { left: 217px; top: 830px; font-size: 30px; font-weight: 300; letter-spacing: 1px; }

  .products { position: absolute; left: 0; top: 874px; width: 400px; margin: 0; padding: 0; list-style: none;
    font-family: "Fira Sans Extra Condensed", sans-serif; font-weight: 700; font-size: 46px; line-height: 48px; color: var(--yellow); }
  .products li { white-space: nowrap; }
  .products li:nth-child(1) { padding-left: 60px; }
  .products li:nth-child(2) { padding-left: 40px; }
  .products li:nth-child(3) { padding-left: 93px; }
  .products li:nth-child(4) { padding-left: 40px; }
  .products li:nth-child(5) { padding-left: 97px; }
  .more { position: absolute; left: 114px; top: 1124px; margin: 0; font-family: "Fira Sans Extra Condensed", sans-serif;
    font-weight: 300; font-size: 27px; line-height: 1; }
</style>
</head>
<body>
<main class="cover">
  <svg class="cover__art" width="848" height="1200" viewBox="0 0 848 1200">
    <defs>
      <linearGradient id="blueField" x1="0" y1="0" x2="0" y2="1">
        <stop offset="0" stop-color="#5f9ed8"/>
        <stop offset="0.4" stop-color="#1f62ae"/>
        <stop offset="1" stop-color="#0d3f86"/>
      </linearGradient>
      <linearGradient id="sweep" x1="0" y1="0" x2="1" y2="1">
        <stop offset="0" stop-color="#dcebf7"/>
        <stop offset="0.5" stop-color="#ffffff"/>
        <stop offset="1" stop-color="#f3f8fc"/>
      </linearGradient>
      <linearGradient id="photoTone" x1="0" y1="0" x2="0" y2="1">
        <stop offset="0" stop-color="#c9cf6a"/>
        <stop offset="0.35" stop-color="#e6e35a"/>
        <stop offset="0.6" stop-color="#8a8f8e"/>
        <stop offset="1" stop-color="#b7b9b6"/>
      </linearGradient>
      <radialGradient id="disc" cx="0.6" cy="0.4" r="0.7">
        <stop offset="0" stop-color="#1a56a2"/>
        <stop offset="1" stop-color="#0b4694"/>
      </radialGradient>
    </defs>
    <rect width="848" height="1200" fill="url(#blueField)"/>
    <rect x="560" y="0" width="288" height="330" fill="#0d4a96"/>
    <path d="M150,0 L585,0 C575,120 585,240 590,330 C470,250 300,150 150,0 Z" fill="url(#sweep)"/>
    <path d="M585,0 C575,120 585,240 590,330 L560,330 C500,250 380,160 250,0 Z" fill="url(#sweep)" opacity="0.6"/>
    <path d="M590,330 L848,330 L848,1200 L350,1200 C370,880 440,560 590,330 Z"
          fill="url(#photoTone)" role="img" aria-label="Photo: yellow bulk bag liner being filled on a warehouse production machine"/>
    <circle cx="150" cy="985" r="270" fill="#3f7fc4"/>
    <circle cx="150" cy="985" r="258" fill="url(#disc)"/>
  </svg>

  <header class="brand">
    <span class="brand__mark"></span>
    <span class="brand__name">TERVIK</span>
    <span class="brand__sub">ENTERPRISES</span>
    <p class="brand__tagline">"Your Source for Bulk Bags, Gaylord Boxes, Liners, Recycling and Much More"</p>
  </header>

  <h1 class="headline">
    <span class="h-quality">Quality</span>
    <span class="h-of">of</span>
    <span class="h-products">Products</span>
    <span class="h-and1">and</span>
    <span class="h-services">Services</span>
    <span class="h-and2">and</span>
    <span class="h-quantity">not the quantity</span>
  </h1>

  <div class="source">
    <span class="s-your">Your #</span>
    <span class="s-source">Source</span>
    <span class="s-one">1</span>
    <span class="s-for">for</span>
  </div>

  <ul class="products">
    <li>Gaylord Boxes,</li>
    <li>FIBC Bulk Bags,</li>
    <li>Stretch Film,</li>
    <li>Packaging Tape,</li>
    <li>Pallets,</li>
  </ul>
  <p class="more">and much more...</p>
</main>
</body>
</html>
```